AUDITING SERVICES FOR IMPORT/EXPORT/LOGISTICS

* PROCUREMENT OF PARTS / SERVICES
* BOAT POSITIONING

Industry/Entity Type

Auditing

Contact Information for Business Card

TRV CONSULTANTS
(TIDEWIND HULLCRAFT PTY LTD) 17 KESTREL VISTA CORALWOOD SHORES
DAVID HARTLEY 0417286342 JULIE-KATE HARTLEY 0417286918 (ON OPPOSITE SIDE)

```html
<!DOCTYPE html>
<html lang="en">
<head>
<meta charset="utf-8">
<title>Procurement of Parts / Services — Boat Positioning</title>
<link rel="stylesheet" href="https://fonts.googleapis.com/css2?family=Cormorant+Garamond:ital,wght@1,500&display=swap">
<style>
  :root {
    --ocean-blue: #238bd0;
    --foam-cyan: #55efff;
    --band-cyan: #52f2fd;
    --text-white: #ffffff;
  }
  html, body {
    margin: 0;
    padding: 0;
    width: 1200px;
    height: 741px;
    overflow: hidden;
  }
  .card {
    position: relative;
    width: 1200px;
    height: 741px;
    overflow: hidden;
    background: var(--ocean-blue);
  }
  .water-texture {
    position: absolute;
    inset: 0;
    background:
      radial-gradient(ellipse at 15% 10%, rgba(85, 239, 255, 0.55), transparent 40%),
      radial-gradient(ellipse at 85% 20%, rgba(85, 239, 255, 0.45), transparent 38%),
      radial-gradient(ellipse at 20% 90%, rgba(85, 239, 255, 0.45), transparent 40%),
      radial-gradient(ellipse at 75% 88%, rgba(85, 239, 255, 0.55), transparent 42%),
      var(--ocean-blue);
  }
  .title-band {
    position: absolute;
    left: 0;
    top: 231px;
    width: 1200px;
    height: 281px;
    background: var(--band-cyan);
  }
  .services {
    position: absolute;
    left: 0;
    width: 1200px;
    margin: 0;
    text-align: center;
    font-family: "Cormorant Garamond", Georgia, serif;
    font-style: italic;
    font-weight: 500;
    font-size: 56px;
    line-height: 1;
    letter-spacing: 0.1em;
    color: var(--text-white);
    white-space: nowrap;
  }
  .services--procurement { top: 285px; }
  .services--positioning { top: 401px; }
</style>
</head>
<body>
  <div class="card">
    <div class="water-texture" role="img" aria-label="Mottled blue and cyan water-surface texture"></div>
    <div class="title-band"></div>
    <p class="services services--procurement">PROCUREMENT OF PARTS / SERVICES</p>
    <p class="services services--positioning">BOAT POSITIONING</p>
  </div>
</body>
</html>
```